7' x 4' sign for a new multiunit residential mountain location**

Our mission is to build people their dream home through the use of professional and thoughtful design. We're a new developer, building a new and feature-filled fourplex, and need a brand and presence that generates interests and builds our brand. Our homes are professionally and thoughtfully designed - we agonize over the details so our homeowners don't have to once they move in.

We're constructing a new fourplex in downtown Kelowna, BC, Canada. The location is in the heart of the city's entertainment and cultural zones, is surrounded by mountains and a lake, and within an hour of over 100 wineries. "Valley" residents prize their time outdoors - boating, biking, hiking, skiing, and more. It's no wonder Kelowna is often cited as one of the most beautiful and desirable places to live in the world.

attachments - brand elements, rendering of the unit, feature sheet for each unit, and picture of the sign casing (7' wide and 4' long envelop - pic of sign frame attached).

Target Market(s)

Young professionals (age 30 to 45); Empty nestes (age 55+)

Font styles to use
Other font styles liked:
• Cordia New

Requirements
Must have
• Our tag line - Home, by design

Presence - this is an unusual shape and large sign. It must create interest and build our brand.

```html
<!DOCTYPE html>
<html lang="en">
<head>
<meta charset="utf-8">
<title>Ridgeline Homes — Kelowna site sign</title>
<link rel="stylesheet" href="https://fonts.googleapis.com/css2?family=Montserrat:wght@800&display=swap">
<style>
  :root {
    --backdrop: #d3d3d1;
    --brand-blue: #00aeef;
    --white: #ffffff;
    --ink: #2b2b2b;
    --pin-red: #e8312f;
  }
  html, body {
    margin: 0;
    padding: 0;
    width: 1200px;
    height: 1200px;
    overflow: hidden;
    background: var(--backdrop);
  }
  .sign {
    display: block;
    width: 1200px;
    height: 1200px;
    font-family: "Montserrat", Arial, sans-serif;
  }
  .sign__panel { fill: var(--brand-blue); }
  .brand-name { fill: var(--white); font-weight: 800; font-size: 128px; }
  .location__bar { fill: var(--white); }
  .location__pin { fill: var(--pin-red); }
  .location__pin-hole { fill: var(--white); }
  .location__name { fill: var(--ink); font-weight: 800; font-size: 63px; }
  .lifestyle__lead { fill: var(--ink); font-weight: 800; font-size: 31px; }
  .lifestyle__list { fill: var(--white); font-weight: 800; font-size: 33px; }
</style>
</head>
<body>
<svg class="sign" viewBox="0 0 1200 1200" xmlns="http://www.w3.org/2000/svg" role="img" aria-label="Ridgeline Homes — Kelowna, BC, Canada site sign">
  <polygon class="sign__panel" points="87,388 600,388 856,226 1112,388 1112,972 87,972"/>

  <text class="brand-name" aria-label="Ridgeline Homes">
    <tspan x="164" y="535" textLength="808" lengthAdjust="spacingAndGlyphs">RIDGELINE</tspan>
    <tspan x="972" y="672" text-anchor="end">HOMES</tspan>
  </text>

  <rect class="location__bar" x="156" y="734" width="888" height="82"/>
  <g class="location__pin">
    <path d="M193,744 C205,744 214,753 214,765 C214,778 203,791 193,806 C183,791 172,778 172,765 C172,753 181,744 193,744 Z"/>
    <circle class="location__pin-hole" cx="193" cy="764" r="7"/>
  </g>
  <text class="location__name" x="222" y="800" textLength="806" lengthAdjust="spacingAndGlyphs">KELOWNA, BC, CANADA</text>

  <text class="lifestyle__lead" x="170" y="884" textLength="860" lengthAdjust="spacingAndGlyphs">"VALLEY" RESIDENTS PRIZE THEIR TIME OUTDOORS -</text>
  <text class="lifestyle__list" x="206" y="926" textLength="788" lengthAdjust="spacingAndGlyphs">BOATING • BIKING • HIKING • SKIING • AND MORE</text>
</svg>
</body>
</html>
```